Brightwave Reach - Business Card

We need a business card for a Social Media Marketing company that specializes in online marketing for small businesses in Canada using common Social Media platforms such as Pictora, Kinloop, Blinkit & Chirpo.

I have uploaded a copy of our logo which I would like utilized in the business card. We would like the business card to be modern yet classy design.

Our website is www.brightwavereach.ca

Industry/Entity Type

Marketing

Contact Information for Business Card

Email: info@brightwavereach.ca
Website: www.brightwavereach.ca
Telephone: 604-392-5108

Colors

Designer to choose colors to be used in the design.

Requirements
Must have
• Social Media icons on reverse
• Please add some designs with color.

```html
<!DOCTYPE html>
<html lang="en">
<head>
<meta charset="utf-8">
<title>Brightwave Reach – Business Card</title>
<link href="https://fonts.googleapis.com/css2?family=Open+Sans:wght@400;600;800&display=swap" rel="stylesheet">
<style>
  :root {
    --stage: #e9e7e6;
    --card-white: #ffffff;
    --card-dark: #3b3d3f;
    --card-dark-back: #3a3e40;
    --green-light: #8dc63f;
    --green-dark: #5b9a2b;
    --ink-grey: #4a4a4a;
    --text-light: #f2f2f2;
    --kinloop-square: #2b4f9e;
    --chirpo-square: #2aa3e6;
  }
  * { box-sizing: border-box; margin: 0; padding: 0; }
  html, body { width: 1200px; height: 800px; overflow: hidden; }
  body {
    background: var(--stage);
    font-family: "Open Sans", Arial, sans-serif;
    position: relative;
  }
  .card {
    position: absolute;
    width: 525px;
    height: 300px;
    top: 250px;
    overflow: hidden;
    box-shadow: 0 10px 28px rgba(0,0,0,0.18);
  }
  .card-front { left: 50px; background: var(--card-white); }
  .card-back { left: 625px; background: var(--card-dark-back); }

  .front-shapes { position: absolute; inset: 0; }

  .brand-mark {
    position: absolute;
    display: flex;
    align-items: center;
    gap: 10px;
    font-weight: 800;
    text-transform: uppercase;
    line-height: 1.05;
  }
  .brand-mark .mark-square {
    width: 16px; height: 16px;
    border: 2px solid currentColor;
    flex: none;
  }
  .front-logo { left: 40px; top: 100px; color: var(--ink-grey); font-size: 24px; width: 180px; }
  .back-logo { left: 50%; top: 95px; transform: translateX(-50%); color: var(--text-light); font-size: 30px; width: 230px; }

  .company-name {
    position: absolute;
    left: 315px; top: 92px;
    color: var(--green-light);
    font-weight: 800;
    font-size: 26px;
    line-height: 1.05;
    text-transform: uppercase;
  }
  .contact-list {
    position: absolute;
    left: 290px; top: 178px;
    list-style: none;
  }
  .contact-list li {
    display: flex;
    align-items: center;
    gap: 10px;
    color: var(--text-light);
    font-size: 13px;
    font-weight: 600;
    height: 28px;
  }
  .contact-icon {
    width: 22px; height: 22px;
    border-radius: 50%;
    background: var(--green-light);
    display: flex; align-items: center; justify-content: center;
    flex: none;
  }

  .social-link {
    position: absolute;
    display: flex;
    align-items: center;
    gap: 8px;
    color: var(--text-light);
    font-size: 12px;
    font-weight: 600;
  }
  .social-link .net-square { width: 12px; height: 12px; border-radius: 2px; flex: none; }
  .social-kinloop { left: 26px; bottom: 24px; }
  .social-kinloop .net-square { background: var(--kinloop-square); }
  .social-chirpo { right: 26px; bottom: 24px; flex-direction: row-reverse; }
  .social-chirpo .net-square { background: var(--chirpo-square); }
</style>
</head>
<body>

<section class="card card-front" aria-label="Business card front">
  <svg class="front-shapes" width="525" height="300" viewBox="0 0 525 300" aria-hidden="true">
    <path d="M258 0 H525 V300 H88 C200 270 290 170 258 0 Z" fill="var(--green-light)"/>
    <path d="M272 0 H525 V300 H118 C228 268 300 170 272 0 Z" fill="var(--green-dark)"/>
    <path d="M284 0 H525 V300 H150 C250 262 312 168 284 0 Z" fill="var(--card-dark)"/>
  </svg>

  <div class="brand-mark front-logo">
    <span class="mark-square"></span>
    <span>Brightwave Reach</span>
  </div>

  <h1 class="company-name">Brightwave<br>Reach</h1>

  <ul class="contact-list">
    <li>
      <span class="contact-icon">
        <svg width="12" height="12" viewBox="0 0 24 24" aria-hidden="true"><path d="M6.6 10.8a15 15 0 0 0 6.6 6.6l2.2-2.2c.3-.3.7-.4 1-.2 1.1.4 2.3.6 3.6.6.6 0 1 .4 1 1V20c0 .6-.4 1-1 1A17 17 0 0 1 3 4c0-.6.4-1 1-1h3.5c.6 0 1 .4 1 1 0 1.3.2 2.5.6 3.6.1.3 0 .7-.2 1z" fill="#fff"/></svg>
      </span>
      604-392-5108
    </li>
    <li>
      <span class="contact-icon">
        <svg width="12" height="12" viewBox="0 0 24 24" aria-hidden="true"><path d="M3 6h18v12H3z" fill="#fff"/><path d="M3 6l9 7 9-7" fill="none" stroke="var(--green-light)" stroke-width="2"/></svg>
      </span>
      info@brightwavereach.ca
    </li>
    <li>
      <span class="contact-icon">
        <svg width="12" height="12" viewBox="0 0 24 24" aria-hidden="true"><g fill="none" stroke="#fff" stroke-width="2"><circle cx="12" cy="12" r="9"/><path d="M3 12h18M12 3c3 3 3 15 0 18M12 3c-3 3-3 15 0 18"/></g></svg>
      </span>
      www.brightwavereach.ca
    </li>
  </ul>
</section>

<section class="card card-back" aria-label="Business card back">
  <div class="brand-mark back-logo">
    <span class="mark-square"></span>
    <span>Brightwave Reach</span>
  </div>

  <div class="social-link social-kinloop">
    <span class="net-square"></span>
    <span>kinloop.com/Brightwave-Reach</span>
  </div>
  <div class="social-link social-chirpo">
    <span class="net-square"></span>
    <span>chirpo.com/search?q=Brightwave-Reach</span>
  </div>
</section>

</body>
</html>
```